Postcard Design

our company name is bramwell court retreat.we provide face to face psychic tarot reading and crystal healing in a very exclusive and private clinic. we provide answers and guidance for future life event and the balance for the body and soul.we are base in 17 osgood lane in london .we want a card who say what we do as clear as possible and who is eye catching to people so when they see it want to read it this is our web site www.bramwellctretreat.co.uk you need to put number on it to call us the number ContacUs:
0208 594 3126
0771 582 3307

Industry/Entity Type

Clinic

```html
<!DOCTYPE html>
<html lang="en">
<head>
<meta charset="utf-8">
<title>Bramwell Court Retreat – Postcard</title>
<link rel="stylesheet" href="https://fonts.googleapis.com/css2?family=Macondo&family=Caladea:wght@400;700&display=swap">
<style>
  :root {
    --frame-dark: #520a6e;
    --frame-light: #8a4aa6;
    --panel: #4f0a72;
    --paper: #ffffff;
    --ink-light: #ffffff;
    --ink-purple: #4a0a66;
    --ink-soft: #6b3a86;
    --rule: #b996cc;
    --photo-warm-a: #7a2a08;
    --photo-warm-b: #e08a1a;
    --photo-cool-a: #6a52c8;
    --photo-cool-b: #a48ae6;
  }
  * { margin: 0; padding: 0; box-sizing: border-box; }
  html, body { width: 1200px; height: 934px; overflow: hidden; background: var(--paper); }
  .postcard { position: relative; width: 1200px; height: 934px; background: var(--paper); }
  .frame {
    position: absolute; left: 16px; top: 13px; width: 1168px; height: 906px;
    background: linear-gradient(90deg, var(--frame-light) 0%, var(--frame-dark) 6%, var(--frame-dark) 100%);
  }
  .frame-inner {
    position: absolute; left: 24px; top: 13px; right: 16px; bottom: 16px;
    background: var(--paper);
  }
  .side-panel {
    position: absolute; left: 46px; top: 38px; width: 409px; height: 855px;
    background: var(--panel);
  }
  .address-photo {
    position: absolute; left: 45px; top: 38px; width: 214px; height: 136px;
    background: radial-gradient(ellipse at 30% 50%, var(--photo-warm-b), var(--photo-warm-a) 80%);
  }
  .address {
    position: absolute; left: 134px; top: 90px;
    font-family: "Macondo", cursive; font-size: 31px; line-height: 38px;
    color: var(--ink-light); text-shadow: 0 0 2px #000, 1px 1px 1px #000;
  }
  .tarot-photo {
    position: absolute; left: 25px; top: 242px; width: 361px; height: 249px;
    background: linear-gradient(135deg, var(--photo-cool-b), var(--photo-cool-a));
  }
  .tagline {
    position: absolute; left: 100px; top: 520px;
    font-family: "Macondo", cursive; font-size: 33px; line-height: 41px;
    color: var(--ink-light);
  }
  .tagline span { display: block; }
  .tagline .l2 { padding-left: 16px; }
  .tagline .l3 { padding-left: 41px; }
  .contact {
    position: absolute; left: 0; width: 409px; top: 690px; text-align: center;
    font-family: "Caladea", serif; font-weight: 700; color: var(--ink-light);
  }
  .contact-title { font-size: 33px; line-height: 44px; margin-left: -30px; }
  .contact-number { font-size: 35px; line-height: 44px; letter-spacing: 2px; margin-left: -30px; }

  .message {
    position: absolute; left: 480px; top: 70px; width: 680px; text-align: center;
    color: var(--ink-purple);
  }
  .brand-name {
    font-family: "Macondo", cursive; font-size: 56px; line-height: 64px;
  }
  .brand-sub {
    margin-top: 6px; font-family: "Caladea", serif; font-size: 22px;
    letter-spacing: 5px; text-transform: uppercase; color: var(--ink-soft);
  }
  .rule { width: 300px; height: 2px; margin: 30px auto; background: var(--rule); }
  .services { list-style: none; font-family: "Macondo", cursive; font-size: 38px; line-height: 58px; }
  .services li::before { content: ""; display: inline-block; width: 10px; height: 10px; margin: 0 16px 8px 0; border-radius: 50%; background: var(--frame-light); }
  .intro {
    margin: 0 auto; width: 560px;
    font-family: "Caladea", serif; font-size: 25px; line-height: 36px; color: var(--ink-soft);
  }
  .cta {
    margin-top: 30px; font-family: "Caladea", serif; font-weight: 700; font-size: 26px; color: var(--ink-purple);
  }
  .website {
    position: absolute; left: 598px; top: 834px;
    font-family: "Macondo", cursive; font-size: 34px; color: var(--ink-purple);
  }
</style>
</head>
<body>
<main class="postcard">
  <div class="frame"><div class="frame-inner"></div></div>
  <section class="side-panel">
    <div class="address-photo" role="img" aria-label="Golden statue in warm orange tones on an ornate background"></div>
    <p class="address">17 Osgood Lane<br>London, UK</p>
    <div class="tarot-photo" role="img" aria-label="Tarot cards laid out on a lilac cloth beside a candle and crystals"></div>
    <p class="tagline"><span class="l1">balance</span><span class="l2">for the body</span><span class="l3">and soul</span></p>
    <div class="contact">
      <p class="contact-title">Contact Us</p>
      <p class="contact-number">0208 594 3126</p>
      <p class="contact-number">0771 582 3307</p>
    </div>
  </section>
  <section class="message">
    <h1 class="brand-name">Bramwell Court Retreat</h1>
    <p class="brand-sub">Exclusive &amp; private clinic</p>
    <div class="rule"></div>
    <ul class="services">
      <li>Psychic Tarot Readings</li>
      <li>Crystal Healing</li>
    </ul>
    <div class="rule"></div>
    <p class="intro">Face to face sessions offering answers and guidance for the events of your future life.</p>
    <p class="cta">Call today to book your private session</p>
  </section>
  <p class="website">www.bramwellctretreat.co.uk</p>
</main>
</body>
</html>
```